Fast Money - Simple Book Cover Design

Hello,

I am in need of a cover for my new book. The Book Title Is

"Standing Builder - Methods for Top Rated Web Feedback That Keeps Your Calendar Full and Draws Fresh Clients Through Your Gates!"

Author: Fireman Dale Prentiss

What I want: This is a book for businesses on improving their online reputation. I want to have 5 Stars on the cover. You can look at this quarvelfind search for ideas of what I am meaning.....

(copy and paste)

http://www.quarvelfind.example/lookup?q=5+star+online+reviews&mode=pics&page=1 (copy and paste)

I am open to different color schemes for the book. I am partial to dark blues if you make it look good. Here is another book that I really like the cover of....

http://www.brindlemart.example/Clipcast-Tactics-Growing-Outreach-ebook/item/ZX93KQ7TWP

I want the cover BOLD and to STAND OUT.

I am looking for a design to help establish me as an authority for online reputation marketing. This book will be both in Pagewell format and be used in print as well.

I am open to questions....

Thanks!

Dale

Reason: I don't believe we have received the right designs. I am going to give everyone more time...

Reason: Hi everyone, I had some stuff come up and was not able to be involved in this project. I am extending because we have not seen the exact thing we want and need time to work with designers to get it right. Thanks Dale

Reason: I am currently traveling and can't wrap this up until I get back.

Target Market(s)

Business Owners

Industry/Entity Type

Business

Requirements
Must have
• Title and Subtitle

Author Name

5 Stars Images....
Nice to have
• Creativity

Bold and stand out

Professional

Should not have
• thin text, small to read text, lame graphics,

```html
<!DOCTYPE html>
<html lang="en">
<head>
<meta charset="utf-8">
<title>Standing Builder — Fireman Dale Prentiss</title>
<link rel="stylesheet" href="https://fonts.googleapis.com/css2?family=Cinzel:wght@400;500;600;700&family=Alegreya+Sans+SC:wght@500;700&display=swap">
<style>
  :root {
    --page-bg: #ffffff;
    --cover-deep: #1e3f7a;
    --cover-mid: #2e5aa0;
    --cover-light: #5f8dcb;
    --wave-light: rgba(160, 200, 240, 0.22);
    --wave-soft: rgba(120, 170, 225, 0.18);
    --ink-light: #eef3fb;
    --ink-soft: #dfe8f6;
    --star-top: #ffe24a;
    --star-bottom: #f0a800;
    --star-edge: #c98600;
    --ribbon-top: #ffd200;
    --ribbon-bottom: #f5a300;
    --ribbon-ink: #e0141b;
    --portrait-top: #d9dde3;
    --portrait-bottom: #a9b6c6;
  }

  * { box-sizing: border-box; margin: 0; padding: 0; }

  html, body {
    width: 1200px;
    height: 1200px;
    overflow: hidden;
    background: var(--page-bg);
  }

  .stage {
    width: 1200px;
    height: 1200px;
    display: flex;
    align-items: center;
    justify-content: center;
  }

  .book-cover {
    position: relative;
    width: 760px;
    height: 1060px;
    overflow: hidden;
    background: linear-gradient(160deg, var(--cover-deep) 0%, var(--cover-mid) 55%, var(--cover-light) 100%);
    color: var(--ink-light);
  }

  .cover-waves {
    position: absolute;
    inset: 0;
    width: 100%;
    height: 100%;
  }

  .author-block {
    position: absolute;
    top: 105px;
    left: 140px;
    display: flex;
    align-items: flex-start;
    gap: 40px;
  }

  .author-portrait {
    width: 165px;
    height: 210px;
    background: linear-gradient(180deg, var(--portrait-top), var(--portrait-bottom));
    border: 3px solid rgba(255, 255, 255, 0.6);
  }

  .author-name {
    font-family: "Cinzel", serif;
    font-weight: 500;
    font-size: 34px;
    letter-spacing: 0.32em;
    line-height: 62px;
    padding-top: 20px;
    color: var(--ink-soft);
  }

  .author-name span { display: block; }

  .book-title {
    position: absolute;
    top: 390px;
    left: 0;
    right: 0;
    text-align: center;
    font-family: "Cinzel", serif;
    font-weight: 400;
    font-size: 112px;
    line-height: 128px;
    letter-spacing: 0.02em;
    color: var(--ink-light);
    text-shadow: 0 2px 6px rgba(10, 25, 60, 0.35);
  }

  .book-title span { display: block; }

  .rating-stars {
    position: absolute;
    top: 690px;
    left: 50%;
    transform: translateX(-50%);
    width: 610px;
    height: 110px;
  }

  .book-subtitle {
    position: absolute;
    top: 850px;
    left: 0;
    right: 0;
    text-align: center;
    font-family: "Alegreya Sans SC", sans-serif;
    font-weight: 700;
    font-size: 33px;
    line-height: 52px;
    letter-spacing: 0.03em;
    color: var(--ink-light);
  }

  .book-subtitle span { display: block; }

  .bestseller-ribbon {
    position: absolute;
    top: 40px;
    right: -95px;
    width: 360px;
    height: 78px;
    transform: rotate(45deg);
    background: linear-gradient(180deg, var(--ribbon-top), var(--ribbon-bottom));
    box-shadow: 0 3px 8px rgba(0, 0, 0, 0.3);
    display: flex;
    align-items: center;
    justify-content: center;
    font-family: "Alegreya Sans SC", sans-serif;
    font-weight: 700;
    font-size: 30px;
    letter-spacing: 0.06em;
    color: var(--ribbon-ink);
  }
</style>
</head>
<body>
<main class="stage">
  <section class="book-cover">
    <svg class="cover-waves" viewBox="0 0 760 1060" preserveAspectRatio="none" aria-hidden="true">
      <path d="M0 620 C 220 520, 420 380, 760 300 L 760 0 L 520 0 C 470 240, 280 470, 0 560 Z" fill="var(--wave-soft)"/>
      <path d="M0 760 C 260 640, 500 560, 760 560 L 760 420 C 520 450, 260 580, 0 700 Z" fill="var(--wave-light)"/>
      <path d="M240 1060 C 380 900, 560 800, 760 760 L 760 1060 Z" fill="var(--wave-soft)"/>
    </svg>

    <div class="author-block">
      <div class="author-portrait" role="img" aria-label="Portrait photo of the author"></div>
      <p class="author-name">
        <span>Fireman</span>
        <span>Dale</span>
        <span>Prentiss</span>
      </p>
    </div>

    <h1 class="book-title">
      <span>STANDING</span>
      <span>BUILDER</span>
    </h1>

    <svg class="rating-stars" viewBox="0 0 610 110" aria-label="Five star rating">
      <defs>
        <linearGradient id="star-fill" x1="0" y1="0" x2="0" y2="1">
          <stop offset="0" stop-color="var(--star-top)"/>
          <stop offset="1" stop-color="var(--star-bottom)"/>
        </linearGradient>
        <path id="star-shape" d="M0 -52 L12.2 -16.8 L49.5 -16.1 L19.8 6.4 L30.6 42.1 L0 20.8 L-30.6 42.1 L-19.8 6.4 L-49.5 -16.1 L-12.2 -16.8 Z"/>
      </defs>
      <g fill="url(#star-fill)" stroke="var(--star-edge)" stroke-width="2" stroke-linejoin="round">
        <use href="#star-shape" x="55" y="58"/>
        <use href="#star-shape" x="180" y="58"/>
        <use href="#star-shape" x="305" y="58"/>
        <use href="#star-shape" x="430" y="58"/>
        <use href="#star-shape" x="555" y="58"/>
      </g>
    </svg>

    <p class="book-subtitle">
      <span>Methods for Top Rated Web Feedback</span>
      <span>That Keeps Your Calendar Full and</span>
      <span>Draws Fresh Clients Through Your Gates!</span>
    </p>

    <div class="bestseller-ribbon">BESTSELLER</div>
  </section>
</main>
</body>
</html>
```